Letterhead Design

We are a physical security and protective intelligence firm based in regional NSW, Australia. We are in need of a professionally designed letter head/ document for our company Valtrix Security. Ref. www.valtrixsecurity.com.au for detailed company information. MUST include Master Licence and ABN details.

Target Market(s)

corporate business, celebrities, property managers, entertainment professionals

Industry/Entity Type

Security

Requirements
Must have
• Must look sharp, professional and cutting edge. Think 419, Silent Directorate, QX3/4 and NOT the movie known as "Dwayne Tuffle Lot Patrol". :-)
Should not have
• Please NO cheesy security guards standing around in uniform. Think protective intelligence and counter terrorism operations. We do not wish to convey an image of a guard company, we offer this service but it is not what we aim to promote. Seek to achieve a higher level approach... elite as opposed to "the usual" guard services etc.

```html
<!DOCTYPE html>
<html lang="en">
<head>
<meta charset="utf-8">
<title>Valtrix Security Letterhead</title>
<link rel="stylesheet" href="https://fonts.googleapis.com/css2?family=Source+Sans+3:wght@400;500;600&display=swap">
<style>
  :root {
    --backdrop: #4a4a4c;
    --paper: #ffffff;
    --tab-black: #0c0c0d;
    --swoosh-grey: #e1e2e2;
    --label-red: #e3232a;
    --ink: #1a1a1a;
    --tag-grey: #d0d0d0;
  }
  * { margin: 0; padding: 0; box-sizing: border-box; }
  html, body {
    width: 1200px; height: 1000px; overflow: hidden;
    background: var(--backdrop);
    font-family: "Source Sans 3", "Helvetica Neue", Arial, sans-serif;
  }
  .letterhead {
    position: absolute; left: 294px; top: 85px;
    width: 602px; height: 845px;
    background: var(--paper);
    overflow: hidden;
  }
  .swoosh { position: absolute; inset: 0; width: 602px; height: 845px; }
  .swoosh path { fill: var(--swoosh-grey); }
  .brand-tab {
    position: absolute; left: 28px; top: 0; width: 174px; height: 90px;
  }
  .brand-tab svg { position: absolute; inset: 0; }
  .brand-tab polygon { fill: var(--tab-black); }
  .brand-name {
    position: absolute; top: 34px; left: 0; width: 174px;
    color: #ffffff;
    font-size: 14px; font-weight: 500; letter-spacing: 0.1px; line-height: 16px;
    display: flex; align-items: center; justify-content: center; gap: 5px;
  }
  .brand-square { width: 7px; height: 7px; background: #ffffff; display: inline-block; }
  .brand-tagline {
    position: absolute; top: 54px; left: 0; width: 174px;
    text-align: center; color: var(--tag-grey); font-size: 6.3px; line-height: 8px;
  }
  .contact-block {
    position: absolute; left: 28px; top: 785px; width: 535px;
    font-size: 9.3px; line-height: 13px; color: var(--ink);
    white-space: nowrap;
  }
  .contact-block .label { color: var(--label-red); }
  .contact-rule {
    position: absolute; left: 28px; top: 825px; width: 535px;
    height: 1.2px; background: var(--ink);
  }
</style>
</head>
<body>
  <div class="letterhead">
    <svg class="swoosh" viewBox="0 0 602 845" aria-hidden="true">
      <path d="M468 0 L481 0 C555 200 590 580 400 845 L291 845 C580 560 540 200 468 0 Z"/>
      <path d="M496 0 L602 0 L602 845 L430 845 C600 580 570 200 496 0 Z"/>
    </svg>

    <header class="brand-tab">
      <svg viewBox="0 0 174 90" width="174" height="90" aria-hidden="true">
        <polygon points="0,0 174,0 174,70 87,90 0,70"/>
      </svg>
      <div class="brand-name"><span class="brand-square"></span>VALTRIX SECURITY</div>
      <div class="brand-tagline">Precision in the Craft of Protection</div>
    </header>

    <footer class="contact-block">
      <div><span class="label">Address:</span>&nbsp; Glenmore New South Wales Australia, 2361</div>
      <div><span class="label">ABN:</span> 51 302 487 119 | <span class="label">Master Licence:</span> 40987 1152 | <span class="label">SIAA Member:</span> 00 07 31 58</div>
      <div><span class="label">Tel:</span> (02) 6700 4182 or 0400 519 264 | <span class="label">Email:</span> office@ValtrixSecurity.com.au | <span class="label">Web:</span> www.valtrixsecurity.com.au</div>
    </footer>
    <div class="contact-rule"></div>
  </div>
</body>
</html>
```